New Web Design Project for kids music school

We need a homepage mockup for a kids' music program. Use your creative talent to come up with something visually appeal and professional for this web-site.

More information is provided in the PDF file called HOME. Also included in this file are links to the photos to be used.

Please let me know if you have more questions.

Target Market(s)

parents

Number of Pages Required

1 page

Font styles to use
Sans Serif

```html
<!DOCTYPE html>
<html lang="en">
<head>
<meta charset="utf-8">
<title>Little Notes – Live Music Education</title>
<link rel="stylesheet" href="https://fonts.googleapis.com/css2?family=Montserrat:wght@600;700;800&family=Lato:wght@400;700&family=Playball&display=swap">
<style>
:root{
  --yellow:#eae33f;
  --red:#f7524a;
  --gold:#f2c12b;
  --teal:#1fc0a8;
  --blue:#2f9fd6;
  --sky:#2ab2dd;
  --ink:#1f1f1f;
  --grey:#7d7d7d;
  --soft:#f5f5f5;
  --white:#fff;
}
*{box-sizing:border-box;margin:0;padding:0}
html,body{width:1200px;height:3885px;overflow:hidden}
body{position:relative;background:var(--white);font-family:'Lato',sans-serif;color:var(--ink)}
.abs{position:absolute}
.script{font-family:'Playball',cursive;font-weight:400}
.btn{position:absolute;display:flex;align-items:center;justify-content:center;border-radius:30px;color:#fff;font-family:'Lato',sans-serif;font-size:13px}

/* top bar */
.topbar{left:0;top:0;width:1200px;height:35px;background:var(--yellow)}
.topbar .contact{left:105px;top:9px;font-size:13px;color:#fff;display:flex;gap:26px}
.topbar .contact span{display:flex;align-items:center;gap:7px}
.social{top:0;height:35px;display:flex;left:951px}
.social i{display:block;width:24px;height:35px;margin-right:1px}

/* nav */
.nav{left:0;top:35px;width:1200px;height:98px;background:#fff}
.brand{left:88px;top:56px;font-family:'Montserrat',sans-serif;font-weight:800;font-size:21px;color:#2a3ea8;line-height:1.05;display:flex;align-items:center;gap:8px}
.brand i{width:14px;height:14px;border-radius:50%;background:var(--gold);display:block}
.menu{top:68px;left:539px;display:flex;align-items:center;font-family:'Montserrat',sans-serif;font-weight:700;font-size:12px;color:#222}
.menu a{text-decoration:none;color:inherit;margin-right:48px}
.menu .active{background:var(--blue);color:#fff;border-radius:20px;padding:9px 22px;margin-right:30px}

/* hero */
.hero{left:0;top:133px;width:1200px;height:473px;background:linear-gradient(100deg,#6f5f56 0%,#9a8c80 35%,#c9b6a4 60%,#b9a58f 80%,#8f7b6c 100%)}
.hero-kicker{left:108px;top:198px;font-size:27px;color:var(--yellow)}
.hero-title{left:106px;top:232px;font-family:'Montserrat',sans-serif;font-weight:700;font-size:53px;line-height:54px;color:#fff}
.hero .signup{}

/* feature cards */
.feature{position:absolute;text-align:center;color:#fff}
.feature .thumb{position:absolute;width:92px;height:92px;border-radius:50%;border:3px solid #fff;left:50%;margin-left:-46px;top:-46px;background:linear-gradient(135deg,#b8a3c9,#e57d88)}
.feature h3{font-family:'Playball',cursive;font-weight:400;font-size:27px;margin-top:56px}
.feature h4{font-family:'Playball',cursive;font-weight:400;font-size:20px;margin-top:4px}
.feature p{font-size:12px;line-height:19px;margin:18px auto 0;width:270px}
.pill{display:inline-flex;align-items:center;justify-content:center;width:136px;height:38px;border-radius:20px;font-size:12px;color:#fff}

/* welcome */
.welcome-img{left:87px;top:878px;width:496px;height:337px;background:linear-gradient(135deg,#d76b8b,#8a6fb1 45%,#e8a73e 75%,#3e6fb3)}
.welcome-title{left:612px;top:882px;font-size:44px;color:var(--red)}
.welcome-text{left:608px;top:952px;width:488px;font-size:13.5px;line-height:20px;color:var(--grey)}

/* stats */
.stats{left:0;top:1280px;width:1200px;height:305px;background:linear-gradient(90deg,#7b8fa1,#b69f8f 40%,#a3b6c8 70%,#6b8aa3)}
.stat{position:absolute;top:1362px;width:140px;text-align:center}
.stat .dia{width:88px;height:88px;transform:rotate(45deg);margin:0 auto;display:flex;align-items:center;justify-content:center}
.stat .dia b{transform:rotate(-45deg);font-family:'Playball',cursive;font-weight:400;font-size:29px;color:#fff}
.stat span{display:block;margin-top:30px;font-family:'Montserrat',sans-serif;font-weight:700;font-size:16px;color:#fff}

/* section titles */
.section-title{position:absolute;left:0;width:1200px;text-align:center;font-size:38px;color:var(--red)}

/* programs */
.program{position:absolute;top:1704px;width:320px;height:467px;background:var(--soft)}
.program .photo{height:201px}
.program .head{display:flex;justify-content:space-between;padding:18px 20px 0 18px}
.program .head h3{font-family:'Playball',cursive;font-weight:400;font-size:20px;color:var(--red)}
.program .head b{font-family:'Montserrat',sans-serif;font-weight:600;font-size:22px;color:var(--gold)}
.program .meta{padding:5px 18px 0;font-size:12px;color:#b0b0b0}
.program p{padding:20px 18px 0;font-size:13px;line-height:20px;color:var(--grey)}
.program .foot{position:absolute;left:0;bottom:0;width:100%;height:52px;display:flex;color:#fff;font-size:16px}
.program .foot span{flex:1;display:flex;align-items:center;justify-content:center}
.program .foot .age{background:var(--red)}
.program .foot .size{background:var(--gold)}

/* videos */
.video{position:absolute;width:316px;height:241px;border-radius:8px;overflow:hidden}
.video svg{position:absolute;left:118px;top:80px}

/* follow */
.follow-mark{left:556px;top:3102px;width:92px;height:92px;border-radius:50%;background:var(--red)}
.gallery{position:absolute;top:3284px;height:234px}

/* map + contact */
.map{left:0;top:3518px;width:1200px;height:217px;background:linear-gradient(90deg,#55595e,#62666b 50%,#585c61)}
.contact-box{left:87px;top:3673px;width:1008px;height:137px;background:#fff;box-shadow:0 6px 18px rgba(0,0,0,.15)}
.contact-box .brand{position:absolute;left:34px;top:44px}
.contact-item{position:absolute;top:50px;display:flex;align-items:center;gap:14px;font-size:29px;color:#111}
.copyright{left:0;top:3840px;width:1200px;text-align:center;font-size:14px;color:#333}
</style>
</head>
<body>

<!-- top bar -->
<div class="abs topbar">
  <div class="abs contact">
    <span><svg width="12" height="12" viewBox="0 0 24 24"><path fill="#fff" d="M6.6 10.8a15 15 0 006.6 6.6l2.2-2.2c.3-.3.7-.4 1-.2 1.1.4 2.3.6 3.6.6.6 0 1 .4 1 1V20c0 .6-.4 1-1 1A17 17 0 013 4c0-.6.4-1 1-1h3.5c.6 0 1 .4 1 1 0 1.3.2 2.5.6 3.6.1.3 0 .7-.2 1z"/></svg>(555) 214-0387</span>
    <span><svg width="13" height="11" viewBox="0 0 24 18"><rect x="1" y="1" width="22" height="16" fill="none" stroke="#fff" stroke-width="2"/><path d="M1 1l11 9 11-9" fill="none" stroke="#fff" stroke-width="2"/></svg>hello@littlenotesmusic.com</span>
  </div>
  <div class="abs social">
    <i style="background:#f0502f"></i><i style="background:#1da7e0"></i><i style="background:#f0502f"></i><i style="background:#1aa3d8"></i>
  </div>
</div>

<!-- nav -->
<div class="abs nav"></div>
<div class="abs brand"><span>Little<br>Notes</span><i></i></div>
<nav class="abs menu">
  <a class="active">HOME</a>
  <a>Live Music Program</a>
  <a>Star Performing Program</a>
  <a>Contact</a>
</nav>

<!-- hero -->
<div class="abs hero" role="img" aria-label="Photo of a smiling toddler in a music class"></div>
<div class="abs hero-kicker script">Welcome to Little Notes</div>
<h1 class="abs hero-title">Live Music Eduation<br>&amp; The Stars!<br>Performing Program</h1>
<div class="btn" style="left:106px;top:412px;width:135px;height:37px;background:var(--gold);font-size:11px">Sign Up</div>

<!-- feature cards -->
<div class="feature" style="left:87px;top:535px;width:325px;height:270px;background:var(--red)">
  <div class="thumb" role="img" aria-label="Photo of children in a live music class"></div>
  <h3>Live Music Program</h3>
  <h4>3 mos. – 3 yrs</h4>
  <p>This "mommy &amp; me" style class is a 45-minute live music adventure.</p>
  <div class="pill" style="background:var(--gold);margin-top:20px">Learn more</div>
</div>
<div class="feature" style="left:412px;top:535px;width:358px;height:281px;background:var(--gold)">
  <div class="thumb" style="background:linear-gradient(135deg,#c9463c,#3f8a4a)" role="img" aria-label="Photo of young performers on stage"></div>
  <h3 style="margin-top:53px">Stars! Performance Program</h3>
  <h4>3 – 14 yrs</h4>
  <p style="margin-top:22px">Kids work once a week to put on a show customized for their class.</p>
  <div class="pill" style="background:var(--red);margin-top:20px">Learn more</div>
</div>
<div class="feature" style="left:770px;top:535px;width:325px;height:270px;background:var(--teal)">
  <div class="thumb" style="background:linear-gradient(135deg,#9fb3c9,#cfd8e3)" role="img" aria-label="Photo of a child in a virtual music lesson"></div>
  <h3>Virtual Music Lessons</h3>
  <p style="margin-top:6px;width:240px">We're now offering one on one virtual music lessons</p>
  <div style="margin-top:12px;font-family:'Montserrat',sans-serif;font-weight:700;font-size:15px;color:#fff">StreamBox</div>
  <div class="pill" style="background:var(--gold);margin-top:16px">Learn more</div>
</div>

<!-- welcome -->
<div class="abs welcome-img" role="img" aria-label="Photo of girls in flower crowns doing a craft"></div>
<h2 class="abs welcome-title script">Welcome to Little Notes</h2>
<p class="abs welcome-text">Teritatis et quasi architecto. Sed ut perspiciatis unde omnis iste natus error sit voluptatem accusantium dolore mque laudantium, totam rem aperiam, eaque ipsa quae ab illo invent. Sed ut perspiciatis unde omnis iste natus error sitdolor sit amet, consectetuer adipiscing elit, sed diam nonummy nibh euismod. Praesent interdum est gravida vehicula est node maecenas loareet morbi a dosis luctus novum est praesent. Magna est consectetur interdum modest dictum.</p>
<div class="btn" style="left:608px;top:1121px;width:172px;height:42px;background:var(--blue)">DISCOVER MORE</div>

<!-- stats -->
<div class="abs stats" role="img" aria-label="Photo of smiling children in class"></div>
<div class="stat" style="left:150px"><div class="dia" style="background:var(--red)"><b>852</b></div><span>Kids</span></div>
<div class="stat" style="left:403px"><div class="dia" style="background:var(--gold)"><b>125</b></div><span>Programs</span></div>
<div class="stat" style="left:657px"><div class="dia" style="background:var(--teal)"><b>32</b></div><span>Trainings</span></div>
<div class="stat" style="left:910px"><div class="dia" style="background:var(--sky)"><b>15</b></div><span>Stars</span></div>

<!-- programs -->
<h2 class="section-title script" style="top:1628px">Our Programs</h2>
<article class="program" style="left:87px">
  <div class="photo" style="background:linear-gradient(135deg,#d9c2a4,#a9b7c4)" role="img" aria-label="Photo of kids at a theater camp"></div>
  <div class="head"><h3>Musical Theater Camps</h3><b>$20</b></div>
  <div class="meta">July-13-16: TBD</div>
  <p>We provide high quality design at vero eos et accusamus et iusto odio dignissimos ducimus qui blanditiis praesentium voluptatum deleniti atque corrupti quos dolores...</p>
  <div class="foot"><span class="age">Age 3-12 years</span><span class="size">Class Size 20</span></div>
</article>
<article class="program" style="left:431px">
  <div class="photo" style="background:linear-gradient(135deg,#3a2a2a,#c23a3a 50%,#3e7b45)" role="img" aria-label="Photo of children in holiday costumes on stage"></div>
  <div class="head"><h3>Star Troopers!</h3><b>$300</b></div>
  <div class="meta">Monday 4:00-5:15PM</div>
  <p>Star Troopers prepare for a short show. They receive a script the second week of class specially written for their class. hey all have a few lines, the chance to do a short solo.</p>
  <div class="foot"><span class="age">Age 5-6 years</span><span class="size">Class Size 20</span></div>
</article>
<article class="program" style="left:775px">
  <div class="photo" style="background:linear-gradient(135deg,#111,#3a3a3a 50%,#151515)" role="img" aria-label="Photo of young actors performing on a dark stage"></div>
  <div class="head"><h3>Acting Allstars!</h3><b>$300</b></div>
  <div class="meta">Grades 1-4 &nbsp;|&nbsp; Monday 4:00-5:15 PM</div>
  <p>Acting Allstars receive a more advanced original script. They have more songs, longer solos, choreography, more lines, and are given more advanced stage direction.They focus on character</p>
  <div class="foot"><span class="age">Age 7-10 years</span><span class="size">Class Size 20</span></div>
</article>
<div class="btn" style="left:497px;top:2217px;width:186px;height:40px;background:var(--red);font-size:12px">SEE MORE CLASSES</div>

<!-- videos -->
<h2 class="section-title script" style="top:2345px">Our Latest StreamBox Videos</h2>
<div class="video" style="left:87px;top:2438px;background:linear-gradient(135deg,#c9b98e,#7c8ea3)" role="img" aria-label="Video still of toddlers singing"><svg width="80" height="80" viewBox="0 0 80 80"><circle cx="40" cy="40" r="36" fill="none" stroke="#fff" stroke-width="6"/><path d="M32 24l24 16-24 16z" fill="#fff"/></svg></div>
<div class="video" style="left:431px;top:2438px;background:linear-gradient(135deg,#b8343a,#2c2a2a 60%,#3f7a44)" role="img" aria-label="Video still of a holiday show"><svg width="80" height="80" viewBox="0 0 80 80"><circle cx="40" cy="40" r="36" fill="none" stroke="#fff" stroke-width="6"/><path d="M32 24l24 16-24 16z" fill="#fff"/></svg></div>
<div class="video" style="left:775px;top:2438px;background:linear-gradient(135deg,#d5708f,#8c6fb0 50%,#e3a648)" role="img" aria-label="Video still of girls in flower crowns"><svg width="80" height="80" viewBox="0 0 80 80"><circle cx="40" cy="40" r="36" fill="none" stroke="#fff" stroke-width="6"/><path d="M32 24l24 16-24 16z" fill="#fff"/></svg></div>
<div class="video" style="left:87px;top:2710px;background:linear-gradient(135deg,#c4b496,#8d97a3)" role="img" aria-label="Video still of a music class"><svg width="80" height="80" viewBox="0 0 80 80"><circle cx="40" cy="40" r="36" fill="none" stroke="#fff" stroke-width="6"/><path d="M32 24l24 16-24 16z" fill="#fff"/></svg></div>
<div class="video" style="left:431px;top:2710px;background:linear-gradient(135deg,#2a2a2a,#8a6f73 50%,#1d1d1d)" role="img" aria-label="Video still of two girls performing"><svg width="80" height="80" viewBox="0 0 80 80"><circle cx="40" cy="40" r="36" fill="none" stroke="#fff" stroke-width="6"/><path d="M32 24l24 16-24 16z" fill="#fff"/></svg></div>
<div class="video" style="left:775px;top:2710px;background:linear-gradient(135deg,#0f0f0f,#383838 50%,#121212)" role="img" aria-label="Video still of a stage performance"><svg width="80" height="80" viewBox="0 0 80 80"><circle cx="40" cy="40" r="36" fill="none" stroke="#fff" stroke-width="6"/><path d="M32 24l24 16-24 16z" fill="#fff"/></svg></div>
<div class="btn" style="left:511px;top:2996px;width:178px;height:40px;background:var(--red)">Visit Channel</div>

<!-- follow -->
<div class="abs follow-mark"></div>
<h2 class="section-title script" style="top:3200px;text-decoration:underline;text-underline-offset:6px;text-decoration-thickness:2px">Follow us on Pixlet</h2>
<div class="gallery" style="left:0;width:241px;background:linear-gradient(135deg,#3c5a86,#d6a88a)" role="img" aria-label="Photo of a teacher and girl reading a book"></div>
<div class="gallery" style="left:241px;width:241px;background:linear-gradient(135deg,#2e4c7a,#9aa9b9)" role="img" aria-label="Photo of two teachers in a classroom"></div>
<div class="gallery" style="left:482px;width:242px;background:linear-gradient(135deg,#b0556f,#d9a4a8)" role="img" aria-label="Photo of two little girls hugging"></div>
<div class="gallery" style="left:724px;width:241px;background:linear-gradient(135deg,#1e1e1e,#8d8d8d)" role="img" aria-label="Black and white photo of a child with headphones"></div>
<div class="gallery" style="left:965px;width:235px;background:linear-gradient(135deg,#e9b535,#7fb3cc)" role="img" aria-label="Photo of a girl in a princess costume"></div>

<!-- map + contact -->
<div class="abs map" role="img" aria-label="Street map showing the school location"></div>
<svg class="abs" style="left:606px;top:3562px" width="56" height="78" viewBox="0 0 56 78"><path d="M28 2C13 2 2 13 2 28c0 20 26 48 26 48s26-28 26-48C54 13 43 2 28 2z" fill="#e8202a"/><circle cx="28" cy="28" r="9" fill="#fff"/></svg>
<div class="abs contact-box">
  <div class="brand"><span>Little<br>Notes</span><i></i></div>
  <div class="contact-item" style="left:232px"><svg width="32" height="32" viewBox="0 0 32 32"><circle cx="16" cy="16" r="16" fill="#1b3fae"/><path fill="#fff" d="M11.5 9l2.5 3.5-1.6 1.8a9 9 0 005.3 5.3l1.8-1.6L23 20.5 21 23c-6 0-12-6-12-12z"/></svg>(555) 214-0387</div>
  <div class="contact-item" style="left:560px"><svg width="36" height="30" viewBox="0 0 36 30"><path d="M1 13L35 1 24 29l-6-11z" fill="#1b3fae"/><path d="M18 18L35 1" stroke="#fff" stroke-width="2"/></svg>hello@littlenotesmusic.com</div>
</div>
<div class="abs copyright">Copyright © 2020 Little Notes!. All rights reserved</div>

</body>
</html>
```